Golden Hearth Talks podcast website redesign

Simple podcast website. Might be similar to marvelow.com (I own this website too so no copyright issues) but I'd like to see fresh ideas too. Here's another simple site that I like: https://plunix.com/

I just need to be able to move all my podcasts over to this website and it not to break anything... I've had a couple of web developers work on it and it needs some work.

I'm not sure how things work on the backend, but the website needs to be able to move all the info from www.goldenhearthtalks.com onto the new webdesign of this project.

Target Market(s)

wives

Number of Pages Required

4 page

Font styles to use
Sans Serif
Script

Colors
fdf0f6
f9d9e8
fee3d4

Requirements
Must have
• Simple (example: https://jodmerrick.com/)
• Lovely (example: marvelow.com)
• A post page, where posts will show up and show a bit about the podcast (like: http://marvelow.com/podcasts/
• On posts I need a podcast audio plugin the post needs to have the audio-bar at the top: https://tunevaultwidget.com/
• I'd really like a lot of space
• Gorgeous mobile (example: https://jodmerrick.com/ looks fantastic in mobile and I really like how it centers and theres a lot of space around in desktop)
• And just as gorgeous desktop
• It should be very easy to change on backend.
Nice to have
• Mostly white space, with some pastels and then black writing. I'd be curious if you have other ideas to "up market" the look. Also, I've attached my current podcast logo, but that is subject to change if the website seems to necessitate it.
Should not have
• Should not be busy. Very simple and elegant and upmarket.

```html
<!DOCTYPE html>
<html lang="en">
<head>
<meta charset="utf-8">
<title>Golden Hearth Talks</title>
<link href="https://fonts.googleapis.com/css2?family=Montserrat:wght@500;600;700;800&family=Lato:ital,wght@0,400;0,700;1,400&family=Allura&display=swap" rel="stylesheet">
<style>
:root{
  --ink:#1d1d1d;
  --text:#555;
  --muted:#777;
  --white:#fff;
  --peach:#fddcca;
  --blush:#f5cfe2;
  --blush-card:#fdeef5;
  --grey-band:#f2f2f2;
  --line:#bdbdbd;
}
*{box-sizing:border-box;margin:0;padding:0}
html,body{width:1200px;height:4380px;overflow:hidden;background:var(--white)}
body{position:relative;font-family:'Lato',sans-serif;color:var(--text)}
.abs{position:absolute}
h2.section-title{font-family:'Montserrat',sans-serif;font-weight:800;color:var(--ink);letter-spacing:1px}

/* hero */
.hero{left:0;top:0;width:1200px;height:592px;background:linear-gradient(100deg,#5d5a52 0%,#8c8577 35%,#b59c86 60%,#7b6a5a 85%,#4e4842 100%)}
.brand{left:110px;top:34px;font-family:'Montserrat',sans-serif;font-weight:700;color:var(--white);font-size:26px;line-height:30px;width:220px}
.top-mail{left:612px;top:32px;color:var(--white);font-size:17px;display:flex;align-items:center;gap:8px}
.btn-outline{border:2px solid var(--white);color:var(--white);border-radius:30px;font-family:'Montserrat',sans-serif;font-weight:700;display:flex;align-items:center;justify-content:center}
.schedule{left:918px;top:20px;width:170px;height:48px;font-size:15px}
.nav{left:407px;top:88px;display:flex;gap:27px;font-family:'Montserrat',sans-serif;font-weight:500;font-size:16px;color:var(--white)}
.nav .active{border-bottom:3px solid var(--white);padding-bottom:8px}
.hero-quote{left:113px;top:205px;width:520px;font-style:italic;font-size:27px;line-height:45px;color:var(--white);font-weight:400}
.get-started{left:109px;top:374px;width:166px;height:60px;font-size:15px}
.dots{left:567px;top:515px;display:flex;gap:4px}
.dots span{width:13px;height:13px;border:2px solid var(--white);border-radius:50%}
.dots span.on{background:var(--white)}

/* about */
.portrait{left:51px;top:697px;width:459px;height:425px;background:linear-gradient(180deg,#d9d9d9,#ececec 70%,#fff)}
.about-title{left:544px;top:700px;font-size:51px}
.about-text{left:544px;top:790px;width:550px;font-size:14.5px;line-height:30px}
.about-text p{margin-bottom:30px}
.signature{left:530px;top:1150px;font-family:'Allura',cursive;font-size:62px;color:var(--ink)}

/* podcast */
.podcast-card{left:110px;top:1355px;width:489px;height:485px;background:var(--peach)}
.podcast-art{left:599px;top:1355px;width:489px;height:485px;background:linear-gradient(180deg,#f6b56e 0%,#d8553d 40%,#8e1e3a 75%,#5c0d2c 100%)}
.podcast-title{left:160px;top:1420px;font-size:51px}
.podcast-sub{left:160px;top:1500px;width:390px;font-family:'Montserrat',sans-serif;font-weight:500;font-size:23px;line-height:37px;color:var(--ink)}
.podcast-text{left:160px;top:1590px;width:400px;font-size:14px;line-height:30px;color:var(--ink)}
.listen{left:161px;top:1714px;width:172px;height:51px;background:var(--ink);color:var(--white);border-radius:30px;font-family:'Montserrat',sans-serif;font-weight:600;font-size:15px;display:flex;align-items:center;justify-content:center;gap:12px}

/* who we are */
.who{left:0;top:1975px;width:1200px;height:694px;background:var(--grey-band)}
.center{left:0;width:1200px;text-align:center}
.who-title{top:2060px;font-size:51px}
.who-text{top:2148px;font-size:14.5px;line-height:30px}
.video{left:348px;top:2256px;width:504px;height:316px;background:linear-gradient(135deg,#8d8d8d,#c7c2bb 50%,#6f6a66);box-shadow:0 6px 14px rgba(0,0,0,.25)}
.play{left:568px;top:2381px}

/* subscribe */
.sub-title{top:2772px;font-size:51px}
.sub-text{top:2862px;font-size:20px;color:#444}
.sub-input{left:241px;top:2927px;width:561px;height:68px;border:1px solid #999;display:flex;align-items:center;gap:10px;padding-left:18px;font-size:18px;color:#555}
.sub-btn{left:802px;top:2927px;width:157px;height:68px;background:var(--ink);color:var(--white);font-family:'Montserrat',sans-serif;font-weight:700;font-size:17px;display:flex;align-items:center;justify-content:center}

/* testimonials */
.testimonials{left:0;top:3118px;width:1200px;height:550px;background:var(--blush)}
.testi-title{top:3202px;font-size:51px}
.card{top:3320px;width:468px;height:235px;background:var(--blush-card);border-radius:4px;padding:22px 20px;box-shadow:0 2px 6px rgba(0,0,0,.06)}
.card h3{font-weight:400;font-size:17px;color:var(--ink);margin-bottom:6px}
.card p{font-style:italic;font-size:13.5px;line-height:28.5px;color:var(--muted)}
.card .who-by{font-family:'Montserrat',sans-serif;font-weight:600;font-size:14px;color:var(--ink);margin-top:14px}

/* contact */
.contact-title{top:3775px;font-size:51px}
.col-label{font-family:'Montserrat',sans-serif;font-weight:500;font-size:21px;color:var(--ink)}
.field{border:1px solid var(--line);border-radius:4px;font-size:13.5px;color:#555;padding:12px 14px}
.submit{left:609px;top:4180px;width:105px;height:41px;background:var(--ink);color:var(--white);border-radius:22px;font-family:'Montserrat',sans-serif;font-weight:700;font-size:13px;display:flex;align-items:center;justify-content:center}
.info-row{left:779px;display:flex;gap:18px;align-items:flex-start;font-size:13.5px;line-height:22px;color:#555}
.ring{width:34px;height:34px;border:1px solid var(--line);border-radius:50%;flex:none;display:flex;align-items:center;justify-content:center}
.social{left:777px;top:4200px;display:flex;gap:12px}
.social span{width:34px;height:34px;border:1px solid #999;border-radius:50%}
.divider{left:110px;top:4275px;width:970px;height:1px;background:#ccc}
.copyright{top:4318px;font-size:13.5px;color:#555}
</style>
</head>
<body>

<!-- hero -->
<div class="abs hero" role="img" aria-label="Photo of a couple touching foreheads at sunset"></div>
<div class="abs brand">Golden Hearth Talks</div>
<div class="abs top-mail">
  <svg width="16" height="12" viewBox="0 0 16 12"><rect x="0.5" y="0.5" width="15" height="11" fill="none" stroke="#fff"/><path d="M1 1l7 6 7-6" fill="none" stroke="#fff"/></svg>
  info@goldenhearthtalks.com
</div>
<div class="abs btn-outline schedule">SCHEDULE A CALL</div>
<nav class="abs nav">
  <span class="active">Home</span><span>About Me</span><span>Testimonials</span><span>Resources</span><span>Podcasts</span><span>For Husbands</span>
  <svg width="16" height="16" viewBox="0 0 16 16" style="margin-top:2px"><circle cx="6.5" cy="6.5" r="5" fill="none" stroke="#fff" stroke-width="2"/><path d="M10 10l5 5" stroke="#fff" stroke-width="2.4"/></svg>
</nav>
<p class="abs hero-quote">It’s more than ok to want a great marriage and amazing sex. In fact, you can do God’s will better when you have both!</p>
<div class="abs btn-outline get-started">GET STARTED</div>
<div class="abs dots"><span class="on"></span><span></span><span></span><span></span></div>

<!-- about -->
<div class="abs portrait" role="img" aria-label="Pencil-style portrait of the host smiling"></div>
<h2 class="abs section-title about-title">ABOUT ME</h2>
<div class="abs about-text">
  <p>Golden Hearth Talks is about going allowing you to not only desire your spouse but feel loved and enjoy the intimacy that God designed for you both!</p>
  <p>If you feel taken for granted, criticized, lonely and sad, sex feels unsafe or maybe a chore, it doesn’t have to be that way! I know--I was there. And I knew, like you, I wasn’t walking in my God-given calling. I was in too much pain. You don’t have to suffer any longer. There really is hope.</p>
  <p>I discovered that intimacy is not only the unifying bond, but adventuresome &amp; fierce, AND safe &amp; peaceful intimacy can each be had in your marriage! Things really can change for you guys, and sex can be better in marriage!</p>
</div>
<div class="abs signature">Marla Quinn</div>

<!-- podcast -->
<div class="abs podcast-card"></div>
<div class="abs podcast-art" role="img" aria-label="Podcast cover art: couple silhouetted against a red sunset with the show title"></div>
<h2 class="abs section-title podcast-title">PODCAST</h2>
<p class="abs podcast-sub">210-Should you tell her about your past sex life?</p>
<p class="abs podcast-text">Do you want unity in your marriage? Do you want her to feel safe to be utterly vulnerable and literally naked before you? Then it is NOT helpful for her to know your past sex life.</p>
<div class="abs listen"><svg width="14" height="16" viewBox="0 0 14 16"><path d="M1 1l12 7-12 7z" fill="#fff"/></svg>LISTEN NOW!</div>

<!-- who we are -->
<div class="abs who"></div>
<h2 class="abs center section-title who-title">WHO WE ARE</h2>
<p class="abs center who-text">Marla Quinn is a marriage and intimacy expert and coach. Her podcast was awarded 19th of the Top 30 Relationship<br>podcasts and she is passionate about helping you have incredible intimacy and joy in your relationship!</p>
<div class="abs video" role="img" aria-label="Video still of the host speaking into a studio microphone"></div>
<svg class="abs play" width="64" height="64" viewBox="0 0 64 64"><circle cx="32" cy="32" r="32" fill="#1d1d1d" opacity=".9"/><path d="M25 19l21 13-21 13z" fill="#fff"/></svg>

<!-- subscribe -->
<h2 class="abs center section-title sub-title">SUBSCRIBE TO STAY IN THE LOOP!</h2>
<p class="abs center sub-text">Enter your email address to get information about us</p>
<div class="abs sub-input">
  <svg width="17" height="13" viewBox="0 0 17 13"><rect width="17" height="13" rx="1" fill="#555"/><path d="M1 1.5l7.5 6 7.5-6" fill="none" stroke="#fff" stroke-width="1.4"/></svg>
  Email Address
</div>
<div class="abs sub-btn">SUBSCRIBE</div>

<!-- testimonials -->
<div class="abs testimonials"></div>
<h2 class="abs center section-title testi-title">TESTIMONIALS</h2>
<svg class="abs" style="left:44px;top:3420px" width="18" height="32" viewBox="0 0 18 32"><path d="M16 2L3 16l13 14" fill="none" stroke="#8a8a8a" stroke-width="2.5"/></svg>
<svg class="abs" style="left:1140px;top:3420px" width="18" height="32" viewBox="0 0 18 32"><path d="M2 2l13 14L2 30" fill="none" stroke="#8a8a8a" stroke-width="2.5"/></svg>
<article class="abs card" style="left:110px">
  <h3>Wow, Just wow!!!</h3>
  <p>So so SO grateful God put her in my path. She is helping me through so many intimacy issues I personally have in my marriage. She is speaking right to the heart and growing my knowledge. I know this is an answered prayer! Love her!</p>
  <div class="who-by">- WIFE</div>
</article>
<article class="abs card" style="left:620px">
  <h3>My marriage has changed...</h3>
  <p>Hi Marla! I just wanted to let you know how much my marriage has changed...We’ve been together for 23 years and married for 17 years, and we feel that we are just scratching the surface of true, unselfish intimacy.</p>
  <div class="who-by">- WIFE</div>
</article>

<!-- contact -->
<h2 class="abs center section-title contact-title">CONTACT US</h2>
<div class="abs col-label" style="left:110px;top:3895px">Contact form</div>
<div class="abs field" style="left:110px;top:3954px;width:298px;height:44px">Name :</div>
<div class="abs field" style="left:418px;top:3954px;width:296px;height:44px">Phone no :</div>
<div class="abs field" style="left:110px;top:4017px;width:604px;height:44px">Email :</div>
<div class="abs field" style="left:110px;top:4077px;width:604px;height:81px">Message :</div>
<div class="abs submit">SUBMIT</div>

<div class="abs col-label" style="left:779px;top:3895px">Contact Information</div>
<div class="abs info-row" style="top:3955px">
  <span class="ring"><svg width="12" height="16" viewBox="0 0 12 16"><path d="M6 15s5-6 5-9.5A5 5 0 001 5.5C1 9 6 15 6 15z" fill="none" stroke="#555" stroke-width="1.4"/><circle cx="6" cy="5.5" r="1.8" fill="#555"/></svg></span>
  <span>4100 Willow Bend Ave, Suite 305<br>Maple Hollow, Oregon 97001</span>
</div>
<div class="abs info-row" style="top:4016px">
  <span class="ring"><svg width="14" height="14" viewBox="0 0 14 14"><path d="M3 1l2.5 3-1.5 1.5c1 2 2.5 3.5 4.5 4.5L10 8.5l3 2.5-1.5 2C6 13 1 8 1 2.5z" fill="#555"/></svg></span>
  <span style="line-height:34px">1 555 010 2040</span>
</div>
<div class="abs info-row" style="top:4076px">
  <span class="ring"><svg width="14" height="11" viewBox="0 0 14 11"><rect width="14" height="11" rx="1" fill="#555"/><path d="M1 1.5l6 5 6-5" fill="none" stroke="#fff" stroke-width="1.2"/></svg></span>
  <span style="line-height:34px">marla@goldenhearthtalks.com</span>
</div>
<div class="abs col-label" style="left:779px;top:4152px">Social Media</div>
<div class="abs social"><span></span><span></span><span></span></div>

<div class="abs divider"></div>
<p class="abs center copyright">Copyright © 2019, Golden Hearth Talks All rights reserved.</p>
<svg class="abs" style="left:1062px;top:4318px" width="28" height="16" viewBox="0 0 28 16"><path d="M2 14L14 3l12 11" fill="none" stroke="#999" stroke-width="2"/></svg>

</body>
</html>
```